Uncoded website + logo for game server company

We're looking to refresh our website - pellarnode.org. We are a server provider that specializes in Blockvale servers, as well as voice servers. Our primary goal is to keep the same essential layout but get a more modern, updated, and smooth look; our current site is a bit cluttered and unprofessional, and doesn't lend too well to ease of use.

Our color scheme is blue and white, though the shade of blue can vary. We are happy to experiment with other colors as well, but blue is recognized as our main color. The shades in use on our current site are a good starting point.

We would like the design to be flat and modern, sleek, and clean. Since we provide services relating to Blockvale, some sort of integration with Blockvale themes would be preferable; eg. elements from the game. The design should not be overly professional as we serve primary a young demographic, but it should still convey a sense of professionalism in that our network and infrastructure is solid.

For our logo, we would like a geometric/cube-based design. We would like to see "PellarNode" used within the logo, rather than "7Node" as it is now. A flat design would be preferred with single or two-tone color scheme using blue/black/white and perhaps other small accent colors. An icon/symbol integrated with the logo would suit us very well.

We would love to keep in contact with the winning designer and continue work on both our current website and other websites in the future.
Please email marlow@pellarnode.org with any additional questions.

** Colors listed are examples that we like, not required **
** No HTML/CSS/JS is required to be submitted; we only need the design. ***

Feel free to submit a single page design for review and we will determine if a full design is necessary. If you choose to do this, please use the home page and/or the Blockvale page.

Target Market(s)

Our target demographic is comprised of young (14 - 24 y/o) gamers and community owners. Because of the audience, the design should be easy to follow and not overly complicated; should be straightforward with its features and options.

Industry/Entity Type

It Company

Font styles to use
Sans Serif

Colors
3276b5
0092cd
ceddec
cde9f5
ecf7fa
ffffff
85abd2

Requirements
Must have
• Required pages:
- Home page with main features and news/updates
- Blockvale page with features and customization options
- Blockvale VPS page, similar to Blockvale page
- Voice servers page with features and customization options
- Dedicated servers page with package listings and features + customization options
- Stub page for other basic pages (ToS/AUP/Careers)

Product pages (Blockvale/voice/dedicated):
- Product overview area with area for summary
- Features area for overview of all included features (such as on current site - see Blockvale)
- Customization options (eg. value sliders) with price display and list of features
Nice to have
• A slider on the front page would be nice, based on HTML elements rather than images as we do not have a graphic designer (utilizing text and background color/texture elements vs fully designed images).
An area for testimonials/quotes from customers
Social icons

```html
<!DOCTYPE html>
<html lang="en">
<head>
<meta charset="utf-8">
<title>PellarNode – Blockvale Server Hosting</title>
<link href="https://fonts.googleapis.com/css2?family=Open+Sans:wght@400;600;700&display=swap" rel="stylesheet">
<style>
:root{
  --blue:#3276b5;
  --blue-dark:#2a65a0;
  --sky:#85abd2;
  --ink:#1a1a1a;
  --text:#222;
  --muted:#888;
  --band:#efefef;
  --page:#fafafa;
  --white:#fff;
  --footer:#2b2b2b;
  --footer-bar:#222;
}
*{box-sizing:border-box;margin:0;padding:0}
html,body{width:1200px;height:2198px;overflow:hidden}
body{position:relative;background:var(--page);font-family:"Open Sans",Arial,sans-serif;color:var(--text)}
.abs{position:absolute}
/* top bar */
.topbar{left:0;top:0;width:1200px;height:33px;background:var(--blue)}
.topbar .btn{position:absolute;top:6px;height:21px;background:var(--white);color:var(--ink);font-size:12px;line-height:21px;padding:0 8px;border-radius:2px}
.tab{right:12px;top:0;width:24px;height:34px;background:var(--sky);border-radius:0 0 12px 12px;color:#fff;text-align:center;font-size:14px;line-height:28px}
/* header */
.header{left:0;top:33px;width:1200px;height:121px;background:var(--white)}
.brand{left:108px;top:62px;display:flex;align-items:center;gap:12px}
.brand-dot{width:40px;height:40px;border-radius:50%;background:var(--blue)}
.brand-name{font-size:34px;font-weight:600;color:var(--blue);line-height:40px}
.subnav{top:47px;font-size:13px;color:var(--sky)}
.subnav span::before{content:"";display:inline-block;width:9px;height:9px;border-radius:50%;background:var(--sky);margin-right:5px}
.nav{top:95px;left:395px;display:flex;gap:0;font-size:15px;color:var(--ink)}
.nav a{color:inherit;text-decoration:none;margin-right:42px;padding-bottom:6px}
.nav a.active{border-bottom:2px solid var(--blue)}
.social-sq{width:28px;height:28px;border:1px solid #ccc;border-radius:3px;background:#fff}
/* title band */
.titleband{left:0;top:154px;width:1200px;height:112px;background:var(--blue);color:#fff}
.crumb{left:112px;top:16px;font-size:14px;font-weight:600}
.crumb b{color:var(--ink);font-weight:600}
.pagetitle{left:110px;top:50px;font-size:35px;font-weight:400}
.intro{left:146px;top:288px;width:900px;font-size:33px;line-height:45px;color:var(--ink)}
.intro em{font-style:normal;color:var(--blue)}
/* features */
.features{left:0;top:412px;width:1200px;height:544px;background:var(--band)}
.feat{width:300px}
.feat h3{display:flex;align-items:center;gap:10px;font-size:22px;font-weight:400;color:var(--blue);margin-bottom:8px}
.feat h3 i{width:30px;height:30px;border-radius:50%;background:#111;flex:none;position:relative}
.feat h3 i::after{content:"";position:absolute;left:9px;top:9px;width:12px;height:12px;border-radius:50%;background:#fff}
.feat p{font-size:12.6px;line-height:24.5px;color:#111}
/* steps */
.easy{left:0;top:984px;width:1200px;text-align:center;font-size:31px;color:var(--ink)}
.easy span{color:var(--blue)}
.step{width:260px;text-align:center}
.step .num{margin:0 auto;width:60px;height:60px;border-radius:50%;background:var(--blue);color:#fff;font-size:30px;line-height:60px;box-shadow:0 3px 5px rgba(0,0,0,.25)}
.step h4{margin-top:23px;font-size:22px;font-weight:400;color:var(--ink)}
.select{left:117px;top:1207px;width:240px;height:39px;border:1px solid var(--blue);background:#fff;font-size:13px;color:var(--muted);line-height:37px;padding-left:14px}
.select .arrow{position:absolute;right:0;top:0;width:38px;height:37px;border-left:1px solid var(--blue)}
.options{left:117px;top:1260px;width:240px;height:226px;border:1px solid var(--blue);background:#fff;font-size:13px;color:var(--muted)}
.options div{height:36.5px;line-height:36.5px;padding-left:13px}
.options .on{background:var(--blue);color:#fff}
.hint{left:360px;top:1178px;width:480px;text-align:center;font-size:11.5px;color:#333}
.username{left:480px;top:1209px;width:238px;height:37px;border:1px solid var(--blue);background:#fff;font-size:13px;color:var(--muted);line-height:35px;padding-left:12px}
.username .q{position:absolute;right:0;top:0;width:38px;height:35px;background:var(--blue)}
.username .q::after{content:"?";position:absolute;left:9px;top:7px;width:21px;height:21px;border-radius:50%;background:#111;color:#fff;font-size:14px;line-height:21px;text-align:center;font-weight:700}
.sl-label{width:300px;text-align:center;font-size:19px;color:var(--ink)}
.slider{width:262px;height:12px;border:1px solid #9ab;border-radius:6px;background:#fff;overflow:hidden}
.slider .fill{height:100%;width:158px;background:repeating-linear-gradient(135deg,var(--blue) 0 5px,#5f9bd0 5px 9px)}
.knob{width:12px;height:24px;background:#fff;border:1px solid #888;border-radius:2px}
.sl-val{font-size:18px;color:var(--ink)}
.cycle{left:843px;width:242px;background:#fff;box-shadow:0 2px 6px rgba(0,0,0,.22)}
.cycle h5{height:52px;line-height:52px;background:var(--blue);color:#fff;text-align:center;font-size:16px;font-weight:700}
.cycle p{padding:9px 13px;font-size:12.6px;line-height:19px;color:#111}
.shadowline{left:110px;top:1612px;width:980px;height:14px;border-radius:50%;box-shadow:0 8px 12px rgba(0,0,0,.35)}
.sum-h{font-size:37px;color:var(--blue);border-bottom:1px solid #bbb;padding-bottom:2px}
.sum-v{font-size:30px;color:var(--ink)}
.order{left:480px;top:1834px;width:238px;height:51px;background:var(--blue);color:#fff;text-align:center;font-size:21px;font-weight:600;line-height:51px;box-shadow:0 2px 4px rgba(0,0,0,.3)}
/* footer */
.footer{left:0;top:1942px;width:1200px;height:220px;background:var(--footer);color:#fff}
.f-label{background:var(--blue);color:#fff;font-size:14px;padding:3px 10px;display:inline-block}
.f-list{font-size:12px;line-height:20px;color:#fff}
.legal{left:416px;top:62px;width:394px;height:126px;background:var(--blue);font-size:10px;line-height:20px;padding:5px 10px;box-shadow:0 2px 5px rgba(0,0,0,.5)}
.f-sq{width:20px;height:20px;background:#fff;border-radius:2px}
.bottombar{left:0;top:2162px;width:1200px;height:36px;background:var(--footer-bar);color:#ddd;font-size:12px}
.count{height:18px;width:74px;background:#4a6ea6;border-radius:2px;font-size:9px;color:#fff;text-align:right;padding-right:6px;line-height:18px}
</style>
</head>
<body>
<div class="abs topbar">
  <span class="btn" style="left:108px">Welcome, guest!</span>
  <span class="btn" style="left:228px">Login</span>
  <span class="btn" style="left:846px">Manage</span>
  <span class="btn" style="left:930px">Support</span>
</div>
<div class="abs tab">+</div>

<div class="abs header"></div>
<div class="abs brand"><div class="brand-dot"></div><div class="brand-name">PellarNode</div></div>
<div class="abs subnav" style="left:697px"><span>Blog</span></div>
<div class="abs subnav" style="left:769px"><span>Server Status</span></div>
<nav class="abs nav">
  <a>Home</a><a class="active">Blockvale</a><a>Voice</a><a>Web</a><a>Dedicated</a><a>FAQ</a>
</nav>
<div class="abs social-sq" style="left:913px;top:88px"></div>
<div class="abs social-sq" style="left:950px;top:88px"></div>

<div class="abs titleband">
  <div class="abs crumb"><b>Home</b> / Blockvale</div>
  <h1 class="abs pagetitle">Blockvale Server Hosting</h1>
</div>

<p class="abs intro">Our shared Blockvale hosting is perfect for servers large and small, with an <em>infinite number of possibilities</em>.</p>

<section class="abs features">
  <div class="abs feat" style="left:132px;top:24px"><h3><i></i>Instant Setup</h3><p>Once your order is placed and paid for, our automated system gets everything setup and ready to go - you'll receive access in less than 5 minutes.</p></div>
  <div class="abs feat" style="left:462px;top:24px"><h3><i></i>Multiforge Panel</h3><p>Our Multiforge control panel gives you ultimate freedom and complete control over your server. Edit config files, upload plugins and mods, stop/start/restart your server with ease.</p></div>
  <div class="abs feat" style="left:791px;top:24px"><h3><i></i>Automated Backups</h3><p>Our 40TB+ system perform remote, off-site backups of your server in all locations. You're free to request restorations or downloads at any time during your service, within the last 5 days.</p></div>
  <div class="abs feat" style="left:132px;top:194px"><h3><i></i>Customization</h3><p>With support for easy Bucketry plugin installation and many popular mods such as Hungry Titan and Gearkit, the possibilities are endless. Want a modpack? Just submit a ticket and we'll take care of the rest.</p></div>
  <div class="abs feat" style="left:462px;top:194px"><h3><i></i>Ultimate Protection</h3><p>Our network is under constant monitoring for attacks, and we actively block any possible threats. With virtually zero security holes and full attack mitigation in many locations, we guarantee server uptime, reliability, and speed.</p></div>
  <div class="abs feat" style="left:791px;top:194px"><h3><i></i>SquareSQL + FTP</h3><p>We support SquareSQL for all plugins and give you full FTP access to your server's files. Manage your databases and files directly from our control panel, plus easy setup for all plugins and mods.</p></div>
  <div class="abs feat" style="left:132px;top:383px"><h3><i></i>Dedicated IPs</h3><p>Starting with 1GB+ plans, you'll receive a unique IP address that isn't shared with other servers. This gives you access to port 25565 and removes any of the hassle with shared IPs.</p></div>
  <div class="abs feat" style="left:462px;top:383px"><h3><i></i>24/7 Support</h3><p>We're always online. You're free to submit a ticket or hop on live chat anytime, with responses usually within less than an hour. If you have any issues with your server, we're here to help.</p></div>
  <div class="abs feat" style="left:791px;top:383px"><h3><i></i>Free Web Hosting</h3><p>All plans 1GB and up come with a free web hosting package - create a small website for your server, or back up some files! Submit a ticket for details.</p></div>
</section>

<h2 class="abs easy" style="font-weight:400">It's easy as 1 2 <span>3</span></h2>

<div class="abs step" style="left:104px;top:1058px"><div class="num">1</div><h4>Server Location</h4></div>
<div class="abs step" style="left:469px;top:1058px"><div class="num">2</div><h4>Configuration</h4></div>
<div class="abs step" style="left:835px;top:1058px"><div class="num">3</div><h4>Billing Cycle</h4></div>

<div class="abs select">Server Location<span class="arrow"><svg width="38" height="37"><path d="M13 15h12l-6 7z" fill="#3276b5"/></svg></span></div>
<div class="abs options">
  <div>Phoenix, Arizona</div><div class="on">Ashburn, Virginia</div><div>Montreal, Quebec</div><div>Roubaix, France</div><div>London, England</div><div>Sydney, Australia</div>
</div>

<p class="abs hint">Enter your Blockvale username so we can automatically OP you!</p>
<div class="abs username">Enter your username<span class="q"></span></div>
<div class="abs sl-label" style="left:449px;top:1256px">Memory</div>
<div class="abs slider" style="left:449px;top:1293px"><div class="fill"></div></div>
<div class="abs knob" style="left:601px;top:1287px"></div>
<div class="abs sl-val" style="left:718px;top:1287px">1GB</div>
<div class="abs sl-label" style="left:449px;top:1322px">Slots</div>
<div class="abs slider" style="left:449px;top:1361px"><div class="fill"></div></div>
<div class="abs knob" style="left:601px;top:1355px"></div>
<div class="abs sl-val" style="left:728px;top:1355px">24</div>

<div class="abs cycle" style="top:1204px"><h5>Monthly</h5><p>Your service will renew once per month, at the normal price.</p></div>
<div class="abs cycle" style="top:1345px"><h5>Quarterly</h5><p>Your service will renew once every 3 months, with a recurring <b>5% discount</b></p></div>
<div class="abs cycle" style="top:1486px"><h5>Semi-annual</h5><p>Your service will renew once every 6 months, with a recurring <b>10% discount</b></p></div>

<div class="abs shadowline"></div>

<div class="abs" style="left:115px;top:1646px"><div class="sum-h" style="width:144px">Location</div><div class="sum-v" style="margin-top:4px">Ashburn, Virginia</div></div>
<div class="abs" style="left:521px;top:1646px"><div class="sum-h" style="width:144px">Memory</div><div class="sum-v" style="margin-top:4px">1GB <span style="color:var(--blue);font-size:22px;margin-left:8px">Slots:</span> <span style="font-size:22px">24</span></div></div>
<div class="abs" style="left:844px;top:1646px;width:250px">
  <div class="sum-h" style="width:144px">Total</div>
  <div style="font-size:48px;color:var(--ink);line-height:58px">$16</div>
  <div style="font-size:17px;font-style:italic;color:var(--ink)">for 1 month ($16/GB)</div>
  <div style="font-size:13px;font-style:italic;color:var(--blue);text-align:right;padding-right:56px;margin-top:8px">You save $2</div>
</div>

<div class="abs order">ORDER NOW</div>

<footer class="abs footer">
  <span class="abs f-label" style="left:141px;top:30px">Links</span>
  <div class="abs f-list" style="left:141px;top:70px">Home<br>Blockvale<br>Voice<br>Web<br>Dedicated<br>FAQ</div>
  <div class="abs f-list" style="left:289px;top:70px">Privacy Policy<br>Terms of Service<br>Report Abuse<br>Jobs<br>About Us<br>Contact Us</div>
  <span class="abs f-label" style="left:416px;top:30px">Legal Notice</span>
  <div class="abs legal">PellarNode is a Blockvale server host providing customers with the best hosting experience possible. PellarNode.org is an entity of PellarNode, LLC, a registered Limited Liability Company in the state of Texas, USA. All trademarks, copyrights and other intellectual properties belong to their respective owners.</div>
  <span class="abs f-label" style="left:841px;top:30px">Social</span>
  <div class="abs f-sq" style="left:841px;top:72px"></div>
  <div class="abs f-sq" style="left:871px;top:72px"></div>
  <div class="abs" style="left:841px;top:104px;font-size:10px;color:#aaa">About 17 hours ago from Chirper</div>
  <div class="abs" style="left:841px;top:124px;width:200px;font-size:11px;line-height:20px">Chillin' with @SomeArcher and @lunavane</div>
</footer>
<div class="abs bottombar">
  <div class="abs" style="left:143px;top:10px">Copyright © 2013 PellarNode, LLC</div>
  <div class="abs count" style="left:846px;top:9px">2,771</div>
  <div class="abs count" style="left:925px;top:9px">4,982</div>
</div>
</body>
</html>
```